Business Card Design and Stationary design for consulting firm

Harbourline Sourcing are looking for a new business card design and a design for their A4 letterhead / A4 invoices.

We are seeking to heavily increase our brand awareness and require a business card that's professional in appearance but also shows flare and innovation. A card design that people will remember.

About Us
Harbourline Sourcing are `The Sourcing Crew’.
Our mission is to be one of Australia’s greatest companies. Our aim is to help our customers achieve the best result from their purchasing experience.

Our Requirement:
• IMPACT! IMPACT! IMPACT!
• BUSINESS & PROFESSIONAL LOOKING

• Our business colours are orange, blue and green (See the logo attached).

We have provided an Art Design specification (attached) that needs to be followed for you to win the design. This also has the font, which is used on the logo.

We are after a two sided business card

Side One should have the:
The company Logo
The Sourcing Crew
www.harbourlinesourcing.com.au
Procure | Personnel | Probity & Privacy
Sydney | Melbourne | Adelaide | Brisbane

Side Two
Logo (optional)
Harbourline Sourcing (optional)
Employee details (details listed below)

The above format is our preferred option, but if you think you can come up with something better, feel free to put it forward.

We are leaving the design up to you, but it must incorporate the logo.

We will need a template that we can change the employee details on, as we will be adding more staff over the coming months.

The details below are for one employee per card with the same design.
------------------------

Employee Details:

Marcus Del Arroyo MBA, MMgmtStratProc
Principal Consultant
0491 372 618
Marcus@harbourlinesourcing.com.au

Brianna Tolley
Consulting Manager
0462 915 308
Brianna@harbourlinesourcing.com.au

Our website is www.harbourlinesourcing.com.au

The Letterhead / invoice needs to incorporate:
the company Logo
The Sourcing Crew
Sydney | Melbourne | Adelaide | Brisbane but otherwise the design is over to you.

This file needs to be delivered in word format as other detail will be added to the documents.

We look forward to you award winning designs. If you require any further information please feel free to contact us.

Regards
Harbourline Sourcing

Target Market(s)

Our Target market is companies with 80+ employees. The market we segment is heavily male based, between the ages of 35-55 years of age.

Industry/Entity Type

Consulting

Contact Information for Business Card

See Project Description

Font styles to use
Other font styles liked:
• See Art Specification

Requirements
Must have
• Company Colours, See Project Description
Should not have
• Be outside the Art specification guidelines

```html
<!DOCTYPE html>
<html lang="en">
<head>
<meta charset="utf-8">
<title>Harbourline Sourcing – Business Card</title>
<link rel="stylesheet" href="https://fonts.googleapis.com/css2?family=Source+Sans+3:wght@400;600;700&display=swap">
<style>
  :root {
    --backdrop: #858585;
    --card: #000000;
    --silver: #d2d2d2;
    --white: #ffffff;
    --brand-blue: #2ba6e1;
    --brand-blue-deep: #2b8ed6;
    --decor-tone: #1c1c1c;
    --text-font: "Source Sans 3", "Myriad Pro", Arial, sans-serif;
  }
  html, body {
    margin: 0;
    padding: 0;
    width: 1200px;
    height: 900px;
    overflow: hidden;
    background: var(--backdrop);
    font-family: var(--text-font);
  }
  .stage {
    position: relative;
    width: 1200px;
    height: 900px;
  }
  .card {
    position: absolute;
    top: 184px;
    height: 490px;
    background: var(--card);
    border-radius: 12px;
    text-align: center;
    color: var(--white);
    overflow: hidden;
  }
  .card--front { left: 299px; width: 301px; }
  .card--back  { left: 645px; width: 305px; }

  .brand-mark {
    position: absolute;
    left: 0;
    right: 0;
    top: 48px;
  }
  .brand-mark__dot {
    display: block;
    width: 72px;
    height: 72px;
    margin: 0 auto 46px;
    border-radius: 50%;
    background: var(--brand-blue);
  }
  .brand-name {
    margin: 0;
    font-weight: 600;
    font-size: 29px;
    color: var(--silver);
    line-height: 1;
    white-space: nowrap;
  }

  .employee {
    position: absolute;
    left: 0;
    right: 0;
    top: 317px;
  }
  .employee__name {
    margin: 0;
    font-size: 17px;
    font-weight: 600;
    color: var(--brand-blue);
    line-height: 22px;
  }
  .employee__credentials {
    margin: 0;
    font-size: 14px;
    font-weight: 400;
    color: var(--brand-blue-deep);
    line-height: 22px;
  }
  .employee__role {
    margin: 0;
    font-size: 14px;
    line-height: 22px;
  }
  .contact {
    position: absolute;
    left: 0;
    right: 0;
    top: 412px;
    font-size: 14px;
    line-height: 21px;
  }
  .contact p { margin: 0; }

  .back-decoration {
    position: absolute;
    left: 0;
    right: 0;
    top: 110px;
    height: 330px;
    background: radial-gradient(ellipse 60% 55% at 50% 45%, var(--decor-tone) 0%, rgba(28,28,28,0.6) 55%, rgba(0,0,0,0) 100%);
  }
  .card--back .brand-name {
    position: absolute;
    left: 0;
    right: 0;
    top: 325px;
    color: var(--white);
    font-size: 31px;
  }
  .website {
    position: absolute;
    left: 0;
    right: 0;
    top: 394px;
    margin: 0;
    font-size: 14px;
    font-weight: 700;
  }
  .services {
    position: absolute;
    left: 0;
    right: 0;
    top: 425px;
    margin: 0;
    font-size: 16px;
    font-weight: 600;
  }
</style>
</head>
<body>
  <main class="stage">
    <section class="card card--front" aria-label="Card front">
      <div class="brand-mark">
        <span class="brand-mark__dot"></span>
        <p class="brand-name">Harbourline Sourcing</p>
      </div>
      <div class="employee">
        <p class="employee__name">Marcus Del Arroyo</p>
        <p class="employee__credentials">MBA, MMgmtStratProc</p>
        <p class="employee__role">Principal Consultant</p>
      </div>
      <div class="contact">
        <p>0491 372 618</p>
        <p>Marcus@harbourlinesourcing.com.au</p>
      </div>
    </section>

    <section class="card card--back" aria-label="Card back">
      <div class="back-decoration" role="img" aria-label="Faint large brand decoration behind the company name"></div>
      <p class="brand-name">Harbourline Sourcing</p>
      <p class="website">www.harbourlinesourcing.com.au</p>
      <p class="services">Procure | Personnel | Probity &amp; Privacy</p>
    </section>
  </main>
</body>
</html>
```